Harrowgate Properties Needs New Stationery Design

We need new clean and white stationery for our property management company based in Winnipeg, Manitoba, Canada. We manage condominium and commercial properties. Additionally, we do real estate development and commercial leasing.

We'll require the following:
- Business cards
- Letterhead*
- Envelope (we mainly use #10, single window envelope)
- Fax Cover Sheet
- *Electronic version of the letterhead that works in Google Docs (.jpg for top header)

Industry/Entity Type

Property Management

```html
<!DOCTYPE html>
<html lang="en">
<head>
<meta charset="utf-8">
<title>Harrowgate Properties – Fax Cover Sheet</title>
<link href="https://fonts.googleapis.com/css2?family=Source+Sans+3:wght@400;700&display=swap" rel="stylesheet">
<style>
  :root {
    --backdrop: #3b3b3b;
    --paper: #ffffff;
    --accent: #1aa3c9;
    --brand: #1f3a7a;
    --ink: #2b2b2b;
    --rule: #3a3a3a;
  }
  * { margin: 0; padding: 0; box-sizing: border-box; }
  html, body {
    width: 1200px; height: 1000px; overflow: hidden;
    background: var(--backdrop);
    font-family: "Source Sans 3", "Helvetica Neue", Arial, sans-serif;
  }
  .fax-sheet {
    position: absolute; left: 276px; top: 105px;
    width: 620px; height: 803px;
    background: var(--paper);
    box-shadow: 0 4px 18px rgba(0,0,0,.45);
  }
  .accent-bar {
    position: absolute; left: 0; top: 39px;
    width: 9px; height: 93px; background: var(--accent);
  }
  .contact-block { position: absolute; left: 0; top: 0; font-size: 11.5px; line-height: 1; }
  .contact-row { position: absolute; display: flex; white-space: nowrap; }
  .contact-label { width: 60px; text-align: right; color: var(--ink); padding-right: 3px; }
  .contact-value { color: var(--accent); }
  .contact-label.inline { width: auto; padding-left: 14px; }
  .brand-name {
    position: absolute; right: 53px; top: 34px;
    text-align: right;
    color: var(--brand); font-weight: 700; font-size: 22px; line-height: 1.0;
  }
  .fax-fields { position: absolute; left: 23px; top: 0; width: 576px; }
  .field-row {
    position: absolute; left: 0; width: 576px; height: 18px;
    display: flex; border-bottom: 1.4px solid var(--rule);
    font-size: 13px; color: var(--ink);
  }
  .field-label { display: block; }
  .field-label.left { width: 290px; }
</style>
</head>
<body>
  <main class="fax-sheet">
    <div class="accent-bar"></div>

    <section class="contact-block">
      <div class="contact-row" style="top:46px"><span class="contact-label">address:</span><span class="contact-value">412 Elmstead Avenue</span></div>
      <div class="contact-row" style="top:59px"><span class="contact-label"></span><span class="contact-value">Winnipeg, MB R3L 4K7</span></div>
      <div class="contact-row" style="top:75px"><span class="contact-label">phone:</span><span class="contact-value">(204) 555-0142</span><span class="contact-label inline">fax:</span><span class="contact-value">(204) 555-0143</span></div>
      <div class="contact-row" style="top:94px"><span class="contact-label">email:</span><span class="contact-value">info@harrowgateproperties.ca</span></div>
      <div class="contact-row" style="top:108px"><span class="contact-label">website:</span><span class="contact-value">www.harrowgateproperties.ca</span></div>
    </section>

    <div class="brand-name">Harrowgate<br>Properties</div>

    <section class="fax-fields">
      <div class="field-row" style="top:165px"><span class="field-label left">To:</span><span class="field-label">From:</span></div>
      <div class="field-row" style="top:197px"><span class="field-label left">Phone:</span><span class="field-label">Phone:</span></div>
      <div class="field-row" style="top:229px"><span class="field-label left">Fax:</span><span class="field-label">Fax:</span></div>
      <div class="field-row" style="top:262px"><span class="field-label left">Date:</span><span class="field-label">Total Pages:</span></div>
      <div class="field-row" style="top:301px"><span class="field-label left">Re:</span><span class="field-label">Cc:</span></div>
    </section>
  </main>
</body>
</html>
```